Business Card and Letterhead for Vantage Psychology

We need a business card design and letterhead to use for our Psychology firm that specializes in psychoeducational assessments and individual therapy. Our motto is Purpose-Driven Assessments, Meaning-Centered Therapy.Our contact information is as follows:
Vantage Psychology
The Marwick Block - 6127-48St.
Box 2716 Olds, AB
T2K 3M8
t 403.555.0148 (VANT)
f 403.555.0172
www.vantagepsychology-example.ca
The business card will be used for two different psychologists so I can supply names nearer to completion. We prefer clean, uncluttered looks.

Target Market(s)

Clients, Educators

Font styles to use
Sans Serif

Colors

Designer to choose colors to be used in the design.

Requirements
Must have
• All relevant contact info, logo, some "white" space.
Nice to have
• It would be nice to see letterhead options that have the logo on the top of the page but also options that have it on the side. I think top of the page is probably our preference.
Should not have
• Too much clutter!

```html
<!DOCTYPE html>
<html lang="en">
<head>
<meta charset="utf-8">
<title>Vantage Psychology — Business Card</title>
<link href="https://fonts.googleapis.com/css2?family=Open+Sans:wght@400;600&display=swap" rel="stylesheet">
<style>
  :root {
    --backdrop: #b9b8b3;
    --card-white: #f6f6f4;
    --brand-blue: #4fb3db;
    --brand-blue-deep: #3c9fc6;
    --accent-orange: #f08a24;
    --ink-grey: #6b6b6b;
  }
  * { margin: 0; padding: 0; box-sizing: border-box; }
  html, body {
    width: 1200px; height: 857px; overflow: hidden;
    background: var(--backdrop);
    font-family: "Open Sans", Arial, sans-serif;
  }
  .stage {
    width: 1200px; height: 857px;
    display: flex; align-items: center; justify-content: center; gap: 60px;
  }
  .card {
    position: relative;
    width: 500px; height: 286px;
    border-bottom: 3px solid var(--accent-orange);
    border-right: 2px solid var(--accent-orange);
    box-shadow: 0 10px 24px rgba(0,0,0,0.18);
  }
  .card--front { background: var(--card-white); }
  .card--back { background: var(--brand-blue); }

  .brand {
    position: absolute; left: 34px; top: 34px;
    display: flex; align-items: center; gap: 10px;
  }
  .brand__dot {
    width: 34px; height: 34px; border-radius: 50%;
    background: var(--brand-blue);
  }
  .brand__name {
    font-size: 15px; font-weight: 600; letter-spacing: 1.5px;
    text-transform: uppercase; color: var(--brand-blue);
  }

  .address {
    position: absolute; left: 34px; top: 96px;
    font-size: 11.5px; line-height: 16px; color: var(--ink-grey);
  }
  .contacts {
    position: absolute; left: 34px; top: 150px;
    list-style: none;
    font-size: 11.5px; line-height: 20px; color: var(--ink-grey);
  }
  .contacts li { display: flex; align-items: center; gap: 8px; }
  .contacts svg { width: 12px; height: 12px; flex: none; }

  .person {
    position: absolute; left: 300px; top: 62px;
    padding-left: 14px;
    border-left: 4px solid var(--accent-orange);
  }
  .person__name {
    font-size: 16px; font-weight: 600; letter-spacing: 0.5px;
    color: var(--brand-blue); text-transform: uppercase; line-height: 20px;
  }
  .person__role { font-size: 11.5px; color: var(--ink-grey); line-height: 16px; }

  .back-mark {
    position: absolute; inset: 0;
    display: flex; flex-direction: column; align-items: center; justify-content: center; gap: 16px;
  }
  .back-mark__ring {
    width: 78px; height: 78px; border-radius: 50%;
    border: 3px solid var(--brand-blue-deep);
  }
  .back-mark__name {
    font-size: 26px; font-weight: 600; letter-spacing: 3px;
    text-transform: uppercase; color: var(--brand-blue-deep);
  }
</style>
</head>
<body>
<main class="stage">
  <section class="card card--front">
    <div class="brand">
      <span class="brand__dot"></span>
      <span class="brand__name">Vantage Psychology</span>
    </div>

    <p class="address">The Marwick Block - 6127-48St.<br>Box 2716 Olds, AB | T2K 3M8</p>

    <ul class="contacts">
      <li>
        <svg viewBox="0 0 12 12"><circle cx="6" cy="6" r="6" fill="var(--accent-orange)"/><path d="M4 3.2l1 1.6-.6.6a4 4 0 0 0 2.2 2.2l.6-.6 1.6 1-.6 1A5 5 0 0 1 3 4z" fill="#fff"/></svg>
        403.555.0148 (VANT)
      </li>
      <li>
        <svg viewBox="0 0 12 12"><circle cx="6" cy="6" r="6" fill="var(--accent-orange)"/><rect x="3.3" y="4.5" width="5.4" height="3.6" fill="#fff"/><rect x="4.3" y="3" width="3.4" height="1.5" fill="#fff"/></svg>
        403.555.0172
      </li>
      <li>
        <svg viewBox="0 0 12 12"><circle cx="6" cy="6" r="6" fill="var(--accent-orange)"/><rect x="3.2" y="4" width="5.6" height="4" fill="#fff"/><path d="M3.2 4l2.8 2.2L8.8 4" stroke="var(--accent-orange)" stroke-width=".7" fill="none"/></svg>
        info@vantagepsychology-example.ca
      </li>
      <li>
        <svg viewBox="0 0 12 12"><circle cx="6" cy="6" r="6" fill="var(--accent-orange)"/><circle cx="6" cy="6" r="3" fill="none" stroke="#fff" stroke-width=".8"/><path d="M3 6h6M6 3v6" stroke="#fff" stroke-width=".6"/></svg>
        www.vantagepsychology-example.ca
      </li>
    </ul>

    <div class="person">
      <p class="person__name">Jordan A. Reyes</p>
      <p class="person__role">Operational Manager</p>
    </div>
  </section>

  <section class="card card--back">
    <div class="back-mark">
      <span class="back-mark__ring"></span>
      <span class="back-mark__name">Vantage Psychology</span>
    </div>
  </section>
</main>
</body>
</html>
```